Civic Counsel and Advocacy Network needs poster design for landlord/tenant cases

We're seeking a poster design (11x17) to spread awareness for services by "Civic Counsel and Advocacy Network". The services they're trying to communicate are regarding housing/landlord/tenant matters.

We'd like the poster to (1) reflect the color scheme and branding of their website www.ccanmorvale.org, (2) contain the following copy: "Everyone needs safe and suitable housing, whether they own a home or rent one. When homelessness threatens, we at CCN help clients free of charge through eviction diversion programs and mortgage/tax foreclosure prevention.", and (3) contain their contact information:

Civic Counsel and Advocacy Network, Inc.
"We are YOUR Law Firm for Housing matters"
Contact us at: (555) 314-2869
housing @ccanmorvale.org
www.ccanmorvale.org

Target Market(s)

People who may be facing eviction or homelessness

Industry/Entity Type

Legal

Colors
0054AA
0677BA
7BADD7
CADEEF
E8F1F8
FFC000
F8CF3A
FAE287
FDF2CF
FEFAEE
EB3D1F
EC4F4E
F09395
F8D3D4
FCEDEE

Requirements
Must have
• Must include colors from website: https://ccanmorvale.org/

```html
<!DOCTYPE html>
<html lang="en">
<head>
<meta charset="utf-8">
<title>Civic Counsel and Advocacy Network – Housing Poster</title>
<link rel="stylesheet" href="https://fonts.googleapis.com/css2?family=Bebas+Neue&family=Montserrat:wght@400;500;800&display=swap">
<style>
  :root {
    --navy: #2f3c8c;
    --navy-deep: #27336f;
    --navy-soft: #4d5ea6;
    --red: #c9473b;
    --red-bright: #d1463a;
    --gold: #a99a62;
    --ink: #2a2b31;
    --body: #3a3b40;
    --paper: #ffffff;
    --stage: #eef0f2;
  }
  * { margin: 0; padding: 0; box-sizing: border-box; }
  html, body {
    width: 1200px; height: 2400px; overflow: hidden;
    background: var(--stage);
  }
  .poster {
    position: absolute; left: 50px; top: 381px;
    width: 1100px; height: 1638px;
    background: var(--paper);
    box-shadow: 0 18px 50px rgba(0,0,0,.22);
    overflow: hidden;
    font-family: "Montserrat", sans-serif;
  }
  .header {
    position: absolute; left: 0; top: 0; width: 100%; height: 256px;
    background: linear-gradient(100deg, var(--navy-soft) 0%, var(--navy) 55%, var(--navy-deep) 100%);
  }
  .brand {
    position: absolute; left: 210px; top: 58px;
    display: flex; align-items: center; gap: 26px;
  }
  .brand-circle {
    width: 140px; height: 140px; border-radius: 50%;
    border: 5px solid #fff;
  }
  .brand-name {
    color: #fff; font-weight: 500; font-size: 31px; line-height: 1.25;
    letter-spacing: 1px; text-transform: uppercase;
    border-bottom: 2px solid #fff; padding-bottom: 6px;
  }
  .backdrop-statue {
    position: absolute; left: 260px; top: 256px; width: 580px; height: 930px;
    background: radial-gradient(ellipse at center, rgba(120,110,100,.10) 0%, rgba(255,255,255,0) 70%);
  }
  .headline {
    position: absolute; left: 0; top: 296px; width: 100%;
    text-align: center; color: var(--ink);
    font-family: "Bebas Neue", "Oswald", sans-serif; font-weight: 400;
    font-size: 158px; line-height: 138px; letter-spacing: 0;
    text-transform: uppercase;
  }
  .headline span { display: block; white-space: nowrap; height: 138px; }
  .tagline-band {
    position: absolute; left: 0; top: 728px; width: 100%; height: 61px;
    background: var(--red);
    color: #fff; text-align: center;
    font-weight: 800; font-size: 37px; line-height: 61px; letter-spacing: 1px;
  }
  .cityscape {
    position: absolute; left: 0; top: 789px; width: 100%; height: 398px;
    background: linear-gradient(90deg, #93a487 0%, #d59b7c 14%, #b77b4d 26%, #7fa5b3 38%, #e6b55c 48%, #b4a08a 55%, #c4b9df 64%, #d8927a 76%, #b97c4f 86%, #8ea8b6 100%);
    opacity: .9;
  }
  .promise {
    position: absolute; left: 0; top: 1208px; width: 100%;
    text-align: center; font-weight: 800; font-size: 64px; line-height: 62px;
    letter-spacing: 1px; text-transform: uppercase;
  }
  .promise .blue { color: var(--navy); display: block; }
  .promise .red { color: var(--red-bright); display: block; }
  .contact-pill {
    position: absolute; left: 124px; top: 1372px; width: 852px; height: 55px;
    border-radius: 28px; overflow: hidden; display: flex;
  }
  .contact-label {
    width: 373px; background: var(--gold); color: #fff;
    font-weight: 500; font-size: 35px; line-height: 55px; text-align: center; letter-spacing: 1px;
  }
  .contact-phone {
    flex: 1; background: var(--red); color: #fff;
    font-weight: 800; font-size: 42px; line-height: 55px;
    display: flex; align-items: center; justify-content: center; gap: 22px; letter-spacing: 1px;
  }
  .contact-phone svg { width: 34px; height: 34px; }
  .links {
    position: absolute; left: 0; top: 1451px; width: 100%;
    display: flex; justify-content: center; gap: 78px;
    font-weight: 500; font-size: 23px; color: var(--ink);
  }
  .links span { display: flex; align-items: center; gap: 10px; }
  .links svg { width: 28px; height: 28px; }
  .statement {
    position: absolute; left: 0; top: 1513px; width: 100%;
    text-align: center; color: var(--body); font-size: 20px; line-height: 25px;
  }
  .skyline {
    position: absolute; left: 0; bottom: 0; width: 100%; height: 150px;
    background: linear-gradient(180deg, rgba(255,255,255,0) 0%, rgba(200,205,212,.35) 100%);
  }
  .rule {
    position: absolute; left: 118px; top: 1584px; width: 864px;
    border-top: 2px dashed var(--navy);
  }
</style>
</head>
<body>
  <main class="poster">
    <header class="header" role="img" aria-label="Deep blue photograph of a judge's gavel">
      <div class="brand">
        <div class="brand-circle"></div>
        <div class="brand-name">Civic Counsel and Advocacy<br>Network Incorporated</div>
      </div>
    </header>

    <div class="backdrop-statue" role="img" aria-label="Faint photograph of a scales of justice statue"></div>

    <h1 class="headline"><span>Everyone needs</span><span>safe and</span><span>suitable housing</span></h1>

    <div class="tagline-band">WHETHER THEY OWN A HOME OR RENT ONE</div>

    <div class="cityscape" role="img" aria-label="Flat illustration of a row of colourful apartment blocks and houses"></div>

    <h2 class="promise">
      <span class="blue">We are your law firm</span>
      <span class="red">for housing matters</span>
    </h2>

    <div class="contact-pill">
      <div class="contact-label">CONTACT US AT:</div>
      <div class="contact-phone">
        <svg viewBox="0 0 24 24" fill="#fff" aria-hidden="true"><path d="M6.6 10.8a15.1 15.1 0 0 0 6.6 6.6l2.2-2.2a1 1 0 0 1 1-.25 11.4 11.4 0 0 0 3.6.57 1 1 0 0 1 1 1V20a1 1 0 0 1-1 1A17 17 0 0 1 3 4a1 1 0 0 1 1-1h3.5a1 1 0 0 1 1 1c0 1.250.2 2.45.57 3.57a1 1 0 0 1-.25 1z"/></svg>
        (555) 314-2869
      </div>
    </div>

    <div class="links">
      <span>
        <svg viewBox="0 0 24 24" fill="none" stroke="#c9473b" stroke-width="2" aria-hidden="true"><rect x="3" y="6" width="18" height="13" rx="1"/><path d="M3 7l9 7 9-7"/></svg>
        housing @ccanmorvale.org
      </span>
      <span>
        <svg viewBox="0 0 24 24" fill="none" stroke="#c9473b" stroke-width="2" aria-hidden="true"><circle cx="12" cy="12" r="9"/><path d="M3 12h18M12 3c3 3 3 15 0 18M12 3c-3 3-3 15 0 18"/></svg>
        www.ccanmorvale.org
      </span>
    </div>

    <p class="statement">When homelessness threatens, we at CCN help clients free of charge through<br>eviction diversion programs and mortgage/tax foreclosure prevention</p>

    <div class="skyline" role="img" aria-label="Faint photograph of a city skyline"></div>
    <div class="rule"></div>
  </main>
</body>
</html>
```